New College Graduate Resume - Creative and unique design that stands out from the rest

Need creative resume design for recent college graduate who graduated from School of Music with a concentration in music composition and production. Striving for a contemporary layout/design that allows the resume to "be unique" and "stand out" but be polished and professional. Open to integrating moderate color/graphics as part of resume design but the design can be minus those attributes as well. Attached is raw content in 7 sections (name/contact info, education, highlights of qualifications, work experience, honors/awards, and professional affiliations). While the designer has full latitude over overall design which (section headers, font type, separation/spacing, use of bullets, justification of text, etc.) please maintain current order/sequence of the 7 sections.

Industry/Entity Type

School

Requirements
Must have
• Name (Tobias Hale Whitcombe II) should be most prominent (bold/font size) compared to remainder of resume copy.
• Section headers should be prominent but less so when compared to name on resume.
• The attached file of resume content is provided as raw source copy and is NOT to be just copied and pasted into open fields as is. Expectation is each section of copy will be organized in a manner that is most visually appealing and may include bullets, appropriate spacing, etc.
Should not have
• The attached file of resume content is provided as source copy and is NOT to be just copied and pasted into open fields as is. Expectation is each section of copy will be organized in a manner that

```html
<!DOCTYPE html>
<html lang="en">
<head>
<meta charset="utf-8">
<title>Tobias Hale Whitcombe II – Resume</title>
<link rel="stylesheet" href="https://fonts.googleapis.com/css2?family=Cabin:wght@400;500;600&family=Cinzel:wght@400;500&family=Lato:wght@400;700&display=swap">
<style>
:root{
  --stage:#ececec;
  --paper:#ffffff;
  --ink:#2b2b2b;
  --muted:#6b6b6b;
  --accent:#29aee6;
  --night:#0e0e0e;
  --charcoal:#353535;
  --light:#d8d8d8;
}
*{box-sizing:border-box;margin:0;padding:0}
html,body{width:1200px;height:900px;overflow:hidden}
body{background:linear-gradient(#fafafa,var(--stage));font-family:"Lato",sans-serif;position:relative}
.resume{position:absolute;left:270px;top:24px;width:660px;height:852px;background:var(--paper);display:flex;box-shadow:0 6px 24px rgba(0,0,0,.18);overflow:hidden}
.sidebar{width:310px;flex:none;height:100%;position:relative;background:linear-gradient(#1b1b1b,var(--night) 40%,#2a2a2a);color:var(--light)}
.sidebar__cap{height:36px;background:var(--charcoal)}
.name-band{height:50px;background:var(--accent);display:flex;align-items:center;padding-left:16px}
.name{font-family:"Cabin",sans-serif;font-weight:500;font-size:25px;color:#fff;letter-spacing:.2px;white-space:nowrap}
.identity{background:var(--charcoal);height:96px;position:relative}
.contact{position:absolute;left:0;top:9px;width:218px;height:78px;background:#fff;color:var(--ink);font-size:10.5px;line-height:1.45;padding:11px 16px}
.contact p+p{margin-top:5px}
.emblem{position:absolute;left:234px;top:9px;width:62px;height:62px;background:#fff;display:flex;align-items:center;justify-content:center}
.sidebar__body{padding:18px 12px 0 26px}
.side-heading{font-family:"Cinzel",serif;color:var(--accent);font-size:13px;font-weight:500;letter-spacing:.3px;position:relative;margin-bottom:6px;white-space:nowrap}
.side-heading::before{content:"";position:absolute;left:-26px;top:3px;width:10px;height:10px;background:var(--accent)}
.profile{font-size:10.5px;line-height:1.42;border-left:1px solid #888;padding-left:10px;margin-bottom:16px}
.edu{list-style:none;font-size:10px;line-height:1.4;margin-bottom:14px}
.edu li{position:relative;padding-left:14px;margin-bottom:6px}
.edu li::before{content:"";position:absolute;left:2px;top:5px;width:5px;height:5px;border-radius:50%;background:#fff}
.edu .degree{display:block;position:relative;padding-left:14px;margin-left:-2px;margin-top:3px}
.edu .degree::before{content:"";position:absolute;left:-12px;top:7px;width:18px;height:1px;background:#fff}
.quals{list-style:none;font-size:11px;line-height:1.32;margin:0 0 9px 16px}
.quals li{position:relative;padding-left:14px}
.quals--left li::before{content:"";position:absolute;left:0;top:3px;border:4px solid transparent;border-right:6px solid #fff;border-left:0}
.quals--bars li::before{content:"";position:absolute;left:0;top:3px;width:6px;height:7px;border-left:2px solid #fff;border-right:2px solid #fff}
.quals--right li::before{content:"";position:absolute;left:0;top:3px;border:4px solid transparent;border-left:6px solid #fff;border-right:0}
.main{flex:1;padding:24px 32px 0 22px;position:relative;color:var(--ink)}
.tab{position:absolute;right:0;width:28px;height:9px;background:var(--accent)}
.main-heading{font-family:"Cinzel",serif;color:var(--accent);font-size:13px;font-weight:500;letter-spacing:.3px;margin:10px 0 6px}
.main-heading:first-child{margin-top:0}
.job{margin-bottom:10px}
.job__title{font-family:"Cabin",sans-serif;font-size:13px;font-weight:500}
.job__meta{font-size:9.5px;color:var(--muted);line-height:1.4;border-left:1px solid #bbb;padding-left:8px;margin:2px 0 4px 8px}
.job__desc{font-size:10px;line-height:1.45;color:#555;border-left:1px solid #bbb;padding-left:8px;margin-left:8px}
.dots{list-style:none;font-size:10.5px;line-height:1.45}
.dots li{position:relative;padding-left:14px}
.dots li::before{content:"";position:absolute;left:2px;top:5px;width:5px;height:5px;border-radius:50%;background:var(--ink)}
</style>
</head>
<body>
<article class="resume">
  <aside class="sidebar">
    <div class="sidebar__cap"></div>
    <header class="name-band"><h1 class="name">Tobias Hale Whitcombe II</h1></header>
    <div class="identity">
      <div class="contact">
        <p>555-014-2286<br>twhitcombe.music@example.com</p>
        <p>218 Linden Crest Road, Atlanta<br>Georgia 30300</p>
      </div>
      <div class="emblem">
        <svg width="40" height="40" viewBox="0 0 40 40" aria-hidden="true">
          <circle cx="20" cy="20" r="19" fill="var(--accent)"/>
          <ellipse cx="17" cy="27" rx="4.2" ry="3.2" fill="#fff"/>
          <rect x="20" y="10" width="1.6" height="17" fill="#fff"/>
          <path d="M21.6 10 q5 3 4 8 q-1-4-4-4z" fill="#fff"/>
        </svg>
      </div>
    </div>
    <div class="sidebar__body">
      <h2 class="side-heading">Profile</h2>
      <p class="profile">Recent graduate of a highly ranked university seeking opportunities to apply composition and production talents across a variety of music genres and other media. Expertise lies in delivering high quality sound design, editing, mixing, and recording. Excellent interpersonal skills and the ability to build strong relationships with people at all levels. Exceptionally motivated self-starter and creative problem solver who enjoys working collaboratively on teams.</p>

      <h2 class="side-heading">Education</h2>
      <ul class="edu">
        <li>Southport University – Larkin School of Music<br>Coral Springs, Florida
          <span class="degree">Bachelor of Music – May 2016<br>Major: Media Writing and Production, GPA 3.20/4.0</span></li>
        <li>Briarwood Academy<br>College Park, Georgia
          <span class="degree">High School Diploma with Honors – May 2011</span></li>
      </ul>

      <h2 class="side-heading">Highlights of Qualifications</h2>
      <ul class="quals quals--left">
        <li>Media Production Software (SoundDesk 11)</li>
        <li>Sound Design</li>
        <li>Sound Acoustics</li>
        <li>Studio Recording</li>
        <li>Audio Editing</li>
      </ul>
      <ul class="quals quals--bars">
        <li>Audio Mixing</li>
        <li>Analog/Digital board operation</li>
        <li>Music Arranging</li>
        <li>Music Composition</li>
        <li>Music Production</li>
      </ul>
      <ul class="quals quals--right">
        <li>Composing Sheet Music</li>
        <li>Singer-songwriter</li>
        <li>Rhythm guitarist</li>
      </ul>
    </div>
  </aside>

  <main class="main">
    <span class="tab" style="top:30px"></span>
    <span class="tab" style="top:236px"></span>
    <span class="tab" style="top:470px"></span>
    <span class="tab" style="top:560px"></span>
    <span class="tab" style="top:655px"></span>
    <span class="tab" style="top:760px"></span>

    <h2 class="main-heading">Work Experience</h2>
    <section class="job">
      <h3 class="job__title">Sound Engineer</h3>
      <p class="job__meta">Harborline Film House (HFH) Miami, FL<br>May 2014 – Present</p>
      <p class="job__desc">Edited and mixed recorded field audio to professional standards. Matched audio with motion picture video to create a seamless product. Recorded automated dialogue replacement (ADR) audio and integrated into motion picture video project using SoundDesk 11. Recorded foley sound effects to be added to film, video, and other media in post-production. Composed and recorded original music to accompany various video projects.</p>
    </section>
    <section class="job">
      <h3 class="job__title">Sales Associate</h3>
      <p class="job__meta">Brightmart Corporation Atlanta, GA<br>May 2013 – October 2013</p>
      <p class="job__desc">Provided customer service, maintained a clean and organized work environment, assisted in sales, and performed cashier responsibilities.</p>
    </section>
    <section class="job">
      <h3 class="job__title">On-Site Promoter/Intern</h3>
      <p class="job__meta">Georgia CAL (Civic Action League)<br>Atlanta, GA<br>June 2012 – August 2012</p>
      <p class="job__desc">Promoted and advertised various campaigns and managed various office tasks, such as setting up site maps and organizing and sorting non-profit donations. Northgate Marketing, Incorporated.</p>
    </section>
    <section class="job">
      <h3 class="job__title">Product Marketing Consultant</h3>
      <p class="job__meta">Atlanta, GA<br>June 2011 – August 2011</p>
      <p class="job__desc">Conducted direct sales and marketing of subsidiary product line through establishing a compelling value proposition, overcoming objections, and closing the sale.</p>
    </section>

    <h2 class="main-heading">Honors/Awards</h2>
    <ul class="dots">
      <li>Best Film and Score: Frights and Frames 2015 Competition (Southport University)</li>
      <li>Everett J Langford Scholar</li>
      <li>Best New Member, Theta Rho Kappa Fraternity, Inc.</li>
      <li>Southport University Homecoming King, 2012</li>
    </ul>

    <h2 class="main-heading">Professional Affiliations</h2>
    <ul class="dots">
      <li>Member, Guild of Contemporary Composers (GCC)</li>
      <li>Member, National Alliance of Composers, Authors, and Publishers (NACAP)</li>
      <li>Member, Sound Engineering Guild (SEG)</li>
      <li>Member, Theta Rho Kappa Fraternity, Incorporated</li>
    </ul>
  </main>
</article>
</body>
</html>
```